Website Redesign /kleiner Spartensender, hauptsächlich Videos
Zielgruppe
85% Männlich, Alter 30 - 65, technikverliebt
Aufgabenstellung
Neuentwicklung der Video-Website.
Mr.KolvoBox ist der erste und einzige unabhängige Zielgruppen-Sender für Neue Medien, Home Entertainment und Satelliten-Kommunikation.
Mit unseren Sendungen informieren wir interessierte Zuschauer sowie Dienstleister und Unternehmen, die sich den Empfang und die Verbreitung digitaler Medien via Satellit, Internet, Kabel oder Mobil auf die Fahne geschrieben haben.
Umsetzung vermutlich mit Wordpress oder Typo3.

```html
<!DOCTYPE html>
<html lang="de">
<head>
<meta charset="utf-8">
<title>Mr.KolvoBox – Video-Website</title>
<link rel="stylesheet" href="https://fonts.googleapis.com/css2?family=PT+Sans+Narrow:wght@400;700&family=Arimo:wght@400;700&display=swap">
<style>
:root{
  --page:#ffffff;
  --band:#e0dfe0;
  --yellow:#f8c400;
  --black:#111111;
  --stage:#3a3a3a;
  --card:#4a4a4a;
  --red:#ff1a0a;
  --teal:#2aa8cc;
  --tv:#5f9de0;
  --phone:#a08d1e;
  --cloud:#1a66cc;
  --white:#ffffff;
}
*{box-sizing:border-box;margin:0;padding:0}
html,body{width:1200px;height:953px;overflow:hidden;background:var(--page)}
body{font-family:"Arimo",Arial,sans-serif;color:var(--white)}
.site{position:relative;width:1145px;height:909px;transform:scale(1.048);transform-origin:0 0}
.abs{position:absolute}
.band{left:0;top:20px;width:1145px;height:470px;background:var(--band)}
.band-yellow{left:120px;top:20px;width:967px;height:470px;background:var(--yellow)}
.brand{left:120px;top:20px;width:287px;height:68px;background:linear-gradient(#bdbdbd,#8d8d8d);display:flex;align-items:center;padding-left:22px;gap:10px}
.brand-dot{width:14px;height:14px;border-radius:50%;background:var(--white)}
.brand-name{font-family:"PT Sans Narrow",sans-serif;font-weight:700;font-size:34px;color:var(--white);letter-spacing:.5px}
.nav{left:120px;top:88px;width:815px;height:26px;background:linear-gradient(#2a2a2a,#050505);display:flex;align-items:center;padding-left:21px;font-family:"PT Sans Narrow",sans-serif;font-weight:700;font-size:13px}
.nav-item{padding:0 7px}
.nav-item:first-child{padding-left:0}
.nav-sep{color:var(--red)}
.login{position:absolute;left:524px;top:4px;display:flex;align-items:center;gap:10px}
.login input{width:104px;height:18px;border:0;background:var(--white)}
.stage{left:120px;top:114px;width:815px;height:376px;background:var(--stage)}
.hero-photo{left:122px;top:122px;width:558px;height:361px;background:linear-gradient(160deg,#5d6a88,#2c3145 45%,#6a5a4e 80%,#3a3230)}
.hero-caption{left:122px;top:395px;width:558px;height:88px;background:rgba(40,40,40,.75);padding:14px 34px;font-size:10.5px;line-height:14px}
.hero-caption h1{font-family:"PT Sans Narrow",sans-serif;font-size:14px;font-weight:700;margin-bottom:12px}
.link{color:var(--red)}
.submenu{left:271px;top:114px;width:81px;background:rgba(30,30,30,.9)}
.submenu li{list-style:none;height:26px;line-height:26px;padding-left:8px;font-family:"PT Sans Narrow",sans-serif;font-weight:700;font-size:11px;border-bottom:1px solid var(--red)}
.submenu li:last-child{border:0}
.teaser{left:682px;width:238px;height:88px;background:linear-gradient(#3e3e3e,#4c4c4c);display:flex;padding:5px 4px;gap:6px;font-size:10.5px;line-height:13px}
.teaser.active{background:linear-gradient(#5c5c5c,#bcbcbc)}
.teaser-thumb{width:111px;height:78px;flex:none;background:linear-gradient(150deg,#566185,#2a2e40 50%,#7a6a5c)}
.teaser h3{font-size:11px;font-weight:700;margin-top:5px}
.teaser p:last-child{margin-top:14px}
.promo{left:121px;top:497px;width:539px;height:69px;background:var(--yellow)}
.card{top:575px;width:173px;height:221px;background:var(--card);padding:7px;font-size:10.5px;line-height:13px}
.card-photo{width:159px;height:120px}
.card h3{font-size:11px;font-weight:700;margin:12px 4px 0}
.card p{margin:0 4px}
.btn{position:absolute;left:7px;bottom:6px;background:var(--teal);font-family:"PT Sans Narrow",sans-serif;font-weight:700;font-size:10px;padding:2px 6px;letter-spacing:.3px}
.cloud{left:300px;top:820px;width:360px;height:67px;background:#f2f4f6;color:var(--cloud);padding:4px 6px;font-size:10px;line-height:16px;overflow:hidden;white-space:normal}
.cloud .s{font-size:7px}.cloud .l{font-size:12px}.cloud .xl{font-size:14px}
.top3{left:680px;top:509px;width:241px;height:371px;background:repeating-linear-gradient(135deg,#eef2f8 0 3px,#dde5f0 3px 4px)}
.top3-title{left:690px;top:514px;font-family:"PT Sans Narrow",sans-serif;font-weight:700;font-size:26px;color:var(--red)}
.callout{left:757px;top:521px;width:158px;height:40px;background:var(--red);font-family:"PT Sans Narrow",sans-serif;font-weight:700;font-size:12px;line-height:14px;padding:5px 10px}
.tab{top:569px;height:26px;font-family:"PT Sans Narrow",sans-serif;font-weight:700;font-size:13px;padding:5px 10px}
.ranking{left:690px;top:595px;width:231px;height:285px;background:var(--red)}
.rank{height:95px;border-bottom:1px dashed var(--white);display:flex;padding:10px 12px;gap:10px}
.rank:last-child{border:0}
.rank-num{font-family:"PT Sans Narrow",sans-serif;font-weight:700;font-size:34px;line-height:34px}
.rank small{display:block;font-family:"PT Sans Narrow",sans-serif;font-weight:700;font-size:11px}
.rank strong{display:block;font-family:"PT Sans Narrow",sans-serif;font-size:12px;margin:2px 0}
.rank p{color:var(--black);font-size:10px;line-height:13px}
</style>
</head>
<body>
<div class="site">
  <div class="abs band"></div>
  <div class="abs band-yellow"></div>
  <div class="abs brand"><span class="brand-dot"></span><span class="brand-name">Mr.KolvoBox</span></div>
  <nav class="abs nav">
    <span class="nav-item">HOME</span><span class="nav-sep">|</span>
    <span class="nav-item">ÜBER MR KOLVO</span><span class="nav-sep">|</span>
    <span class="nav-item">PROGRAMM</span><span class="nav-sep">|</span>
    <span class="nav-item">PARTNER</span><span class="nav-sep">|</span>
    <span class="nav-item">KONTAKT</span><span class="nav-sep">|</span>
    <span class="nav-item">PRESSE</span>
    <div class="login"><span>LOGIN</span><input aria-label="Benutzer"><input aria-label="Passwort" type="password"><span>OK</span></div>
  </nav>
  <div class="abs stage"></div>
  <div class="abs hero-photo" role="img" aria-label="Foto der Moderatorinnen der aktuellen Sendung"></div>
  <div class="abs hero-caption">
    <h1>HEADLINE ZUR AKTUELLEN SENDUNG</h1>
    <p>Hier steht ein Text zur aktuellen Sendung. Hier steht ein Text zur aktuellen Sendung. Hier steht ein Text zur aktuellen Sendung. Hier steht ein Text zur aktuellen Sendung. &gt;&gt; <span class="link">ansehen</span></p>
  </div>
  <ul class="abs submenu"><li>SUBMENU</li><li>SUBMENU</li><li>SUBMENU</li><li>SUBMENU</li></ul>

  <div class="abs teaser" style="top:122px"><div class="teaser-thumb" role="img" aria-label="Vorschaubild der Sendung"></div><div><h3>Hier steht ein Text</h3><p>Hier steht ein Text zur aktuellen Sendung</p><p>&gt;&gt; <span class="link">ansehen</span></p></div></div>
  <div class="abs teaser active" style="top:214px"><div class="teaser-thumb" role="img" aria-label="Vorschaubild der Sendung"></div><div><h3>Hier steht ein Text</h3><p>Hier steht ein Text zur aktuellen Sendung</p><p>&gt;&gt; <span class="link">ansehen</span></p></div></div>
  <div class="abs teaser" style="top:306px"><div class="teaser-thumb" role="img" aria-label="Vorschaubild der Sendung"></div><div><h3>Hier steht ein Text</h3><p>Hier steht ein Text zur aktuellen Sendung</p><p>&gt;&gt; <span class="link">ansehen</span></p></div></div>
  <div class="abs teaser" style="top:396px"><div class="teaser-thumb" role="img" aria-label="Vorschaubild der Sendung"></div><div><h3>Hier steht ein Text</h3><p>Hier steht ein Text zur aktuellen Sendung</p><p>&gt;&gt; <span class="link">ansehen</span></p></div></div>

  <div class="abs promo"></div>

  <article class="abs card" style="left:121px"><div class="card-photo" role="img" aria-label="Foto einer nachdenklichen Frau" style="background:linear-gradient(#ffffff,#e8dfe4 60%,#8a3c8a)"></div><h3>Hier steht ein Text</h3><p>Hier steht ein Text zur aktuellen Sendung</p><span class="btn">ENROLL NOW</span></article>
  <article class="abs card" style="left:304px"><div class="card-photo" role="img" aria-label="Foto eines Paares im Abendoutfit" style="background:linear-gradient(120deg,#2a2e3a,#4a4f60 50%,#b0202a)"></div><h3>Hier steht ein Text</h3><p>Hier steht ein Text zur aktuellen Sendung</p><span class="btn">GO NOW</span></article>
  <article class="abs card" style="left:487px"><div class="card-photo" role="img" aria-label="Foto zweier Personen hinter einem Laptop" style="background:linear-gradient(#eef0f2,#d9dcdf)"></div><h3>Hier steht ein Text</h3><p>Hier steht ein Text zur aktuellen Sendung</p><span class="btn">WATCH NOW</span></article>

  <div class="abs cloud"><span class="s">animals</span> architecture <span class="l">art</span> <span class="s">asia</span> australia baby <span class="s">band barcelona</span> <span class="l">beach</span> <span class="s">berlin bike bird birds</span> <span class="l">birthday</span> black <span class="s">blackandwhite</span> blue bw <span class="xl">california</span> canada <span class="xl">lumen</span> <span class="s">car</span> cat chicago <span class="l">china</span> christmas <span class="s">church</span> city <span class="s">clouds club color</span> concert <span class="s">cute dance day</span> de do england europe <span class="s">fall</span> <span class="l">family</span> <span class="s">fashion</span> festival film florida flower flowers food</div>

  <div class="abs top3"></div>
  <div class="abs top3-title">top3</div>
  <div class="abs callout">KURZE ERKLÄRUNG ZU DEM JEWEILIGEN MEDIUM</div>
  <div class="abs tab" style="left:690px;width:72px;background:var(--red)">WEB</div>
  <div class="abs tab" style="left:764px;width:73px;background:var(--tv)">TV</div>
  <div class="abs tab" style="left:839px;width:73px;background:var(--phone)">PHONE</div>
  <ol class="abs ranking">
    <li class="rank"><span class="rank-num">1</span><div><small>SUBHEADLINE</small><strong>HEADLINE</strong><p>Hier steht der Inhalt zu der Headline Hier steht der Inhalt zu der Headline</p></div></li>
    <li class="rank"><span class="rank-num">2</span><div><small>SUBHEADLINE</small><strong>HEADLINE</strong><p>Hier steht der Inhalt zu der Headline Hier steht der Inhalt zu der Headline</p></div></li>
    <li class="rank"><span class="rank-num">3</span><div><small>SUBHEADLINE</small><strong>HEADLINE</strong><p>Hier steht der Inhalt zu der Headline Hier steht der Inhalt zu der Headline</p></div></li>
  </ol>
</div>
</body>
</html>
```